Microdosing Magic Mushrooms book cover

Hello!
I need a 5.25x8 PLV paperback cover and RUB audiobook square cover with the same design. (I might need a Spanish copy as well, but that should just be copy and pasting the translation after the winner is chosen, so don't worry about that for now.)
The title text should be laid out something like this:
A QUICK
WHAT, WHO, WHY, WHERE, HOW & WHEN
-----OF-----
MICRODOSING
MAGIC MUSHROOMS
The book should be about 160 pages, for the spine width.
I have attached some concepts/ideas I have for inspiration, but feel free to submit any kinds of ideas you might have. I'm open to your creativity!
~~~~~~~~
Back Sleeve Summary:
Countless studies and anecdotal reports have shown that large doses of psilocybin mushrooms can inspire breakthroughs and mystical experiences or help relieve symptoms of mental health disorders and physical ailments. However, macrodosing psychedelics doesn’t always have a practical application in our day-to-day lives.
Enter microdosing: a method of taking small amounts of psychedelics to invoke a desirable physiological response with minimal undesirable drawbacks. The practice has become more popular in recent years and is proving to be a safe and powerful approach not only to addressing an array of health concerns but also to improving general performance.
Whether you’re looking to taper off pharmaceuticals or simply improve your mood, creativity, sleep, eating habits, physical stamina, or sexual performance, this book will help you learn how microdosing could improve your overall quality of life. The information herein also doesn’t shy away from addressing more controversial topics, such as microdosing in youth or during pregnancy.
This book is intended to provide foundational knowledge of what microdosing is, who is doing it, various motivations for doing so, ideal times and protocols for practice, considerations for where to microdose, and how to go about sourcing and dosing psilocybin mushrooms. It is a carefully researched, beginner-friendly guide that weaves together concise history and research with practical application and integration of microdosing psilocybin.
Author Section (with attached photo):
Dorian Plaskett earned a B.S. in Kinesiology from the University of Halvermont, and has furthered his studies in the fields of psychedelics, psychology, and trauma healing since 2012. He’s been exploring the benefits of psychedelics within himself for equally as long.
People interested in self help, healing, and microdosing psychedelics.

```html
<!DOCTYPE html>
<html lang="en">
<head>
<meta charset="utf-8">
<title>A Gentle When, Where, Why, How, Who &amp; What of Low-Dosing Spirit Fungi — Book Cover</title>
<link rel="stylesheet" href="https://fonts.googleapis.com/css2?family=Permanent+Marker&family=Barlow+Semi+Condensed:wght@600&family=Inter:wght@400&display=swap">
<style>
  :root {
    --backdrop: #b9b9b9;
    --cover-dark: #2a2a2d;
    --pill-white: #f1f1f3;
    --glow-pink: #e0339a;
    --title-pink: #ff3f9e;
    --title-purple: #5a22a8;
    --title-blue: #1f8ef0;
    --text-white: #ffffff;
    --body-grey: #e6e6ea;
    --night-blue: #1d2a4a;
    --shroom-red: #a8324a;
    --shroom-cyan: #39b9ff;
    --shroom-violet: #8a3ad0;
    --shroom-gold: #f2b640;
  }
  * { box-sizing: border-box; margin: 0; padding: 0; }
  html, body { width: 669px; height: 1200px; overflow: hidden; }
  body { background: var(--backdrop); position: relative; font-family: "Inter", sans-serif; }

  /* ---------- Front cover (em-scaled, 26em x 41.6em) ---------- */
  .front-cover {
    position: absolute;
    width: 26em; height: 41.6em;
    background: var(--cover-dark);
    overflow: hidden;
  }
  .front-cover--hero { left: 166px; top: 88px; font-size: 12px; box-shadow: 0 10px 30px rgba(0,0,0,.35); }
  .front-cover--wrap { left: 272px; top: 0; font-size: 9.5px; }

  .title-pill {
    position: absolute;
    left: 19.4%; top: 11.5%;
    width: 68.7%; height: 75.3%;
    background: var(--pill-white);
    border-radius: 9em;
    box-shadow: 0 0 1.6em 0.5em var(--glow-pink);
    display: flex; flex-direction: column; align-items: center; justify-content: center;
    text-align: center;
    font-family: "Permanent Marker", sans-serif;
    line-height: 1.05;
    padding: 0 1em;
    white-space: nowrap;
  }
  .title-lead { color: var(--title-pink); font-size: 2.3em; }
  .title-questions { color: var(--title-purple); font-size: 1.75em; margin-top: .15em; }
  .title-divider {
    display: flex; align-items: center; width: 100%; margin: .6em 0 .5em;
  }
  .title-divider::before, .title-divider::after {
    content: ""; flex: 1; height: 2px;
    background: linear-gradient(90deg, var(--title-purple), var(--title-pink));
  }
  .title-of {
    width: 1.7em; height: 1.7em; border-radius: 50%;
    background: var(--title-pink); color: var(--text-white);
    font-size: .9em; display: flex; align-items: center; justify-content: center;
  }
  .title-method { color: var(--title-blue); font-size: 1.95em; }
  .title-key { color: var(--title-pink); font-size: 4em; line-height: 1.05; }
  .title-subject { color: var(--title-blue); font-size: 2.4em; }

  .author-name {
    position: absolute; right: 9%; bottom: 3.2%;
    font-family: "Barlow Semi Condensed", sans-serif; font-weight: 600;
    color: var(--text-white); font-size: 2.2em; white-space: nowrap;
  }

  .mushroom-art { position: absolute; opacity: .85; border-radius: 45%; }
  .mushroom-art--left { left: 2%; top: 38%; width: 30%; height: 60%;
    background: linear-gradient(180deg, var(--shroom-red), var(--shroom-cyan) 35%, var(--shroom-red) 62%, var(--shroom-gold) 85%, transparent); border-radius: 40%; }
  .mushroom-art--right { left: 84%; top: 36%; width: 18%; height: 26%;
    background: linear-gradient(180deg, var(--shroom-violet), var(--shroom-cyan) 60%, var(--shroom-gold)); }
  .mushroom-art--corner { left: 74%; top: 78%; width: 28%; height: 24%;
    background: linear-gradient(180deg, var(--shroom-red), var(--shroom-cyan) 60%, transparent); }

  /* ---------- Flat wrap (back, spine, front) ---------- */
  .cover-wrap {
    position: absolute; left: 75px; top: 740px;
    width: 519px; height: 396px;
    background: var(--cover-dark);
    overflow: hidden;
  }
  .back-cover { position: absolute; left: 0; top: 0; width: 247px; height: 396px; }
  .back-night {
    position: absolute; inset: 0;
    background: radial-gradient(ellipse at 55% 10%, var(--night-blue), transparent 70%),
                linear-gradient(180deg, transparent 60%, rgba(40,48,90,.5) 75%, transparent 90%);
  }
  .back-title {
    position: absolute; left: 0; top: 24px; width: 100%;
    text-align: center; font-family: "Permanent Marker", sans-serif; line-height: 1.15;
  }
  .back-title .bt-lead { color: var(--title-pink); font-size: 12px; }
  .back-title .bt-questions { color: var(--text-white); font-size: 8px; }
  .back-title .bt-of { color: var(--title-pink); font-size: 5px; }
  .back-title .bt-method { color: var(--title-blue); font-size: 17px; }
  .back-title .bt-subject { color: var(--title-pink); font-size: 17px; }
  .blurb {
    position: absolute; left: 25px; top: 118px; width: 194px;
    color: var(--body-grey); font-size: 3.9px; line-height: 1.55; text-align: justify;
  }
  .blurb p { margin-bottom: 5px; text-align-last: center; }
  .author-photo {
    position: absolute; left: 26px; top: 278px; width: 45px; height: 45px;
    background: linear-gradient(160deg, #d9d9d9, #6c6c6c);
  }
  .author-bio-name {
    position: absolute; left: 79px; top: 278px;
    font-family: "Barlow Semi Condensed", sans-serif; font-weight: 600;
    color: var(--title-blue); font-size: 11px; white-space: nowrap;
  }
  .author-bio {
    position: absolute; left: 79px; top: 295px; width: 140px;
    color: var(--body-grey); font-size: 4px; line-height: 1.6;
  }

  .spine {
    position: absolute; left: 247px; top: 0; width: 25px; height: 396px;
    writing-mode: vertical-rl;
    display: flex; align-items: center;
    padding-top: 16px;
    font-family: "Permanent Marker", sans-serif; line-height: 1;
    white-space: nowrap;
  }
  .spine-lead { color: var(--title-pink); font-size: 10px; }
  .spine-questions { color: var(--text-white); font-size: 4.4px; line-height: 1.25; margin-top: 5px; }
  .spine-of { color: var(--title-pink); font-size: 5px; margin: 3px 0; }
  .spine-method { color: var(--title-blue); font-size: 10px; }
  .spine-subject { color: var(--title-pink); font-size: 10px; margin-top: 5px; }
  .spine-author {
    margin-top: auto; margin-bottom: 16px;
    font-family: "Barlow Semi Condensed", sans-serif; font-weight: 600;
    color: var(--text-white); font-size: 8.5px;
  }
</style>
</head>
<body>

<section class="front-cover front-cover--hero" aria-label="Front cover">
  <div class="mushroom-art mushroom-art--left" role="img" aria-label="Illustrated glowing mushroom cluster"></div>
  <div class="title-pill">
    <div class="title-lead">A GENTLE</div>
    <div class="title-questions">WHEN, WHERE,<br>WHY, HOW,<br>WHO &amp; WHAT</div>
    <div class="title-divider"><span class="title-of">of</span></div>
    <div class="title-method">LOW-DOSING</div>
    <div class="title-key">SPIRIT</div>
    <div class="title-subject">FUNGI</div>
  </div>
  <div class="mushroom-art mushroom-art--right" role="img" aria-label="Illustrated spotted mushroom cap"></div>
  <div class="mushroom-art mushroom-art--corner" role="img" aria-label="Illustrated mushroom stems"></div>
  <div class="author-name">Dorian Plaskett</div>
</section>

<section class="cover-wrap" aria-label="Full cover wrap">
  <div class="back-cover">
    <div class="back-night" role="img" aria-label="Faint night forest background"></div>
    <div class="back-title">
      <div class="bt-lead">A GENTLE</div>
      <div class="bt-questions">WHEN, WHERE, WHY, HOW, WHO &amp; WHAT</div>
      <div class="bt-of">of</div>
      <div class="bt-method">LOW-DOSING</div>
      <div class="bt-subject">SPIRIT FUNGI</div>
    </div>
    <div class="blurb">
      <p>Countless studies and anecdotal reports have shown that large doses of psilocybin mushrooms can inspire breakthroughs and mystical experiences or help relieve symptoms of mental health disorders and physical ailments. However, macrodosing psychedelics doesn’t always have a practical application in our day-to-day lives.</p>
      <p>Enter microdosing: a method of taking small amounts of psychedelics to invoke a desirable physiological response with minimal undesirable drawbacks. The practice has become more popular in recent years and is proving to be a safe and powerful approach not only to addressing an array of health concerns but also to improving general performance. Whether you’re looking to taper off pharmaceuticals or simply improve your mood, creativity, sleep, eating habits, physical stamina, or sexual performance, this book will help you learn how microdosing could improve your overall quality of life. The information herein also doesn’t shy away from addressing more controversial topics, such as microdosing in youth or during pregnancy.</p>
      <p>This book is intended to provide foundational knowledge of what microdosing is, who is doing it, various motivations for doing so, ideal times and protocols for practice, considerations for where to microdose, and how to go about sourcing and dosing psilocybin mushrooms. It is a carefully researched, beginner-friendly guide that weaves together concise history and research with practical application and integration of microdosing psilocybin.</p>
    </div>
    <div class="author-photo" role="img" aria-label="Author portrait photo"></div>
    <div class="author-bio-name">Dorian Plaskett</div>
    <p class="author-bio">earned a B.S. in Kinesiology from the University of Halvermont, and has furthered his studies in the fields of psychedelics, psychology, and trauma healing since 2012. He’s been exploring the benefits of psychedelics within himself for equally as long.</p>
  </div>

  <div class="spine">
    <span class="spine-lead">A GENTLE</span>
    <span class="spine-questions">WHEN, WHERE, WHY,<br>HOW, WHO &amp; WHAT</span>
    <span class="spine-of">of</span>
    <span class="spine-method">LOW-DOSING</span>
    <span class="spine-subject">SPIRIT FUNGI</span>
    <span class="spine-author">Dorian Plaskett</span>
  </div>

  <div class="front-cover front-cover--wrap">
    <div class="mushroom-art mushroom-art--left" role="img" aria-label="Illustrated glowing mushroom cluster"></div>
    <div class="title-pill">
      <div class="title-lead">A GENTLE</div>
      <div class="title-questions">WHEN, WHERE,<br>WHY, HOW,<br>WHO &amp; WHAT</div>
      <div class="title-divider"><span class="title-of">of</span></div>
      <div class="title-method">LOW-DOSING</div>
      <div class="title-key">SPIRIT</div>
      <div class="title-subject">FUNGI</div>
    </div>
    <div class="mushroom-art mushroom-art--right" role="img" aria-label="Illustrated spotted mushroom cap"></div>
    <div class="mushroom-art mushroom-art--corner" role="img" aria-label="Illustrated mushroom stems"></div>
    <div class="author-name">Dorian Plaskett</div>
  </div>
</section>

</body>
</html>
```